Web Design for ROLV Air conditioning company

Hello,

I am calling on you for the modernization of the company's website
https://clarovent-services-techniques.fr/

The new one must include the new logo with the new graphic charter (color, style ...)

I'm looking for a simple design (less is more), a font written without Serif, the logo that brings a touch of color and modernity.

(maintenance and installation company for air conditioning and ventilation systems)
COLORS: in line with the logo

CHAPTER:

# PRESENTATION
# SERVICES
AIR CONDITIONING (ice cube icon)
HEATING (flame icon)
AIR TREATMENT (icon fan)
# ACHIEVEMENTS

# CONTACT
CONTACT FORM
GOOGLE MAPS

Target Market(s)

Showcase site for our customers

Coding

Coded - Design and coding required

Number of Pages Required

4 page

Font styles to use
Sans Serif

Colors
33b8a4
33a6d7
3176b5
ffffff

Requirements
Must have
• Clear and fluid navigation
a visual identity of the page with the logo
Should not have
• Overloaded.

```html
<!DOCTYPE html>
<html lang="en">
<head>
<meta charset="utf-8">
<title>ROLV – Air Conditioning &amp; Maintenance</title>
<link href="https://fonts.googleapis.com/css2?family=Poppins:wght@400;500;600;700;800&display=swap" rel="stylesheet">
<style>
:root{
  --teal:#33b8a4;
  --blue:#33a6d7;
  --deep:#3176b5;
  --white:#ffffff;
  --ink:#2f3b48;
  --text:#3d3d3d;
  --muted:#6b6b6b;
  --paper:#eeeceb;
  --soft:#f3f2f2;
}
*{margin:0;padding:0;box-sizing:border-box}
html,body{width:1200px;height:3926px;overflow:hidden}
body{position:relative;font-family:'Poppins',sans-serif;color:var(--text);background:var(--white)}
.abs{position:absolute}
a{text-decoration:none;color:inherit}

/* header */
.site-header{position:absolute;left:0;top:0;width:1200px;height:95px;background:var(--white);box-shadow:0 2px 6px rgba(0,0,0,.08);z-index:5}
.brand{position:absolute;left:67px;top:18px;display:flex;align-items:center;gap:10px}
.brand-mark{width:14px;height:14px;background:var(--teal)}
.brand-name{font-family:'Poppins',sans-serif;font-weight:800;font-size:48px;line-height:1;color:var(--ink);letter-spacing:1px}
.main-nav{position:absolute;left:408px;top:38px;display:flex;gap:27px;font-size:14px;color:var(--ink);font-weight:500}
.main-nav .active{color:var(--teal);padding-bottom:8px;border-bottom:2px solid var(--teal)}
.caret{font-size:9px;margin-left:4px;vertical-align:middle}
.hotline{position:absolute;left:918px;top:20px;display:flex;align-items:center;gap:10px}
.hotline small{display:block;color:var(--teal);font-size:13px;font-weight:500}
.hotline strong{display:block;color:var(--ink);font-size:21px;font-weight:700;line-height:1.1}

/* hero */
.hero-copy{position:absolute;left:130px;top:305px;color:#1d1d1d}
.hero-copy h1{font-size:32px;font-weight:800;line-height:40px;text-transform:uppercase}
.hero-copy p{font-size:20px;font-weight:500;line-height:29px;margin-top:20px;text-transform:uppercase}
.btn{display:inline-flex;align-items:center;justify-content:center;font-size:15px;font-weight:600;text-transform:uppercase}
.btn-fill{position:absolute;left:132px;top:484px;width:156px;height:44px;background:linear-gradient(90deg,var(--teal),var(--deep));color:var(--white)}
.btn-light{position:absolute;left:304px;top:484px;width:156px;height:44px;background:var(--white);color:#222}
.slider-arrow{position:absolute;top:382px;width:48px;height:48px;border-radius:50%}

/* about */
.lead-line{position:absolute;height:2px;border-top:2px dashed var(--blue)}
.lead-dot{position:absolute;width:10px;height:10px;border-radius:50%;background:var(--blue)}
.about-title{position:absolute;left:130px;top:862px;font-size:42px;font-weight:800;color:var(--deep);line-height:1}
.about-title span{color:var(--blue)}
.about-sub{position:absolute;left:130px;top:926px;font-size:17px;font-weight:600;color:#555;text-transform:uppercase}
.about-text{position:absolute;left:130px;top:968px;width:470px;font-size:16.5px;line-height:26px;color:#444}
.about-text p+p{margin-top:14px}
.btn-outline{position:absolute;height:48px;border:2px solid var(--teal);border-radius:24px;color:var(--teal);font-size:15px;font-weight:600}

/* services */
.services{position:absolute;left:0;top:1328px;width:1200px;height:614px;background:var(--paper)}
.section-title{position:absolute;width:1200px;text-align:center;font-weight:800;text-transform:uppercase}
.services .section-title{top:76px;font-size:46px;color:var(--ink)}
.section-title .accent{color:var(--teal)}
.service-card{position:absolute;top:189px;width:300px;height:300px;border-radius:50%;background:var(--ink);border:4px solid #26313c;color:var(--white);text-align:center}
.service-card.featured{background:var(--blue);border-color:#2b8fc0}
.service-card .icon{position:absolute;left:114px;top:30px}
.service-card h3{position:absolute;top:122px;width:100%;font-size:20px;font-weight:600;text-transform:uppercase}
.service-card p{position:absolute;top:158px;left:45px;width:202px;font-size:12px;line-height:19px;color:#c9d1d8}
.service-card.featured p{color:#dff2fb}
.service-card .more{position:absolute;left:130px;top:231px}

/* spirit */
.spirit{position:absolute;left:0;top:1942px;width:1200px;height:558px;overflow:hidden}
.spirit-copy{position:absolute;left:131px;top:98px;color:var(--white)}
.spirit-copy h2{font-size:30px;font-weight:800;text-transform:uppercase;line-height:1}
.spirit-copy .sub{font-size:15px;font-weight:500;margin-top:15px;text-transform:uppercase}
.checklist{list-style:none;margin-top:25px}
.checklist li{display:flex;align-items:center;gap:16px;font-size:15.5px;font-weight:600;text-transform:uppercase;height:38.5px}

/* climate */
.climate{position:absolute;left:0;top:2500px;width:1200px;height:636px;background:var(--ink);color:var(--white)}
.climate .section-title{top:80px;font-size:38px}
.title-rule{position:absolute;left:572px;top:140px;width:56px;height:3px;background:var(--white)}
.feature{position:absolute;width:250px;color:var(--white)}
.feature h4{font-size:23px;font-weight:500;line-height:1.2;color:var(--white)}
.feature p{font-size:13px;line-height:19px;margin-top:12px;letter-spacing:-.3px;color:var(--white)}
.feature .btn-line{display:inline-flex;align-items:center;justify-content:center;width:110px;height:36px;border:2px solid var(--white);font-size:14px;margin-top:14px;color:var(--white)}
.feature.right-align{text-align:right}
.icon-disc{position:absolute;width:96px;height:96px;border-radius:50%;background:var(--white);display:flex;align-items:center;justify-content:center}
.hub-name{position:absolute;left:470px;top:2825px;width:216px;text-align:center;font-size:60px;font-weight:800;color:var(--white);line-height:1}

/* contact */
.contact{position:absolute;left:0;top:3136px;width:1200px;height:440px;background:var(--soft)}
.contact .section-title{top:70px;font-size:34px;color:var(--teal)}
.field{position:absolute;background:var(--white);font-size:16px;color:#555;padding:11px 20px}

/* footer */
.footer-brand{position:absolute;left:138px;top:3662px;display:flex;align-items:center;gap:12px}
.footer-brand .brand-name{font-size:82px}
.footer-brand .brand-mark{width:22px;height:22px}
.socials{position:absolute;left:160px;top:3766px;display:flex;gap:8px}
.socials span{width:32px;height:32px;border-radius:50%;border:2px solid var(--deep)}
.foot-col{position:absolute;top:3650px;font-size:14px;color:#666}
.foot-col h5{font-size:20px;font-weight:600;color:#222;text-transform:uppercase;margin-bottom:8px}
.foot-col li{list-style:none;line-height:27px}
.contact-row{display:flex;gap:8px;align-items:flex-start;line-height:21px;margin-bottom:12px}
.legal{position:absolute;left:0;top:3862px;width:1200px;border-top:1px solid #ddd;text-align:center;padding-top:24px;font-size:14px;color:#555}
</style>
</head>
<body>

<header class="site-header">
  <a class="brand" href="https://clarovent-services-techniques.fr/"><span class="brand-mark"></span><span class="brand-name">ROLV</span></a>
  <nav class="main-nav">
    <a class="active">HOME</a><a>ABOUT</a><a>SERVICES<span class="caret">▼</span></a><a>ACHIEVEMENTS</a><a>CONTACT</a>
  </nav>
  <div class="hotline">
    <svg width="52" height="52" viewBox="0 0 52 52"><circle cx="26" cy="26" r="23" fill="none" stroke="var(--deep)" stroke-width="3"/><path d="M18 15c2-1 4 4 4 6s-2 2-1 4 4 6 6 7 2-1 4-1 6 3 5 5-3 3-5 3c-8-1-16-10-16-18 0-3 1-5 3-6z" fill="var(--deep)"/></svg>
    <div><small>24/7 fast service</small><strong>1 800 555 0199</strong></div>
  </div>
</header>

<!-- hero -->
<svg class="abs" style="left:0;top:95px" width="1200" height="685" viewBox="0 0 1200 685">
  <defs>
    <linearGradient id="heroPhoto" x1="0" y1="0" x2="1" y2="1">
      <stop offset="0" stop-color="#f1efec"/><stop offset=".45" stop-color="#dcd8d3"/><stop offset=".75" stop-color="#8da0b8"/><stop offset="1" stop-color="#c9c6c3"/>
    </linearGradient>
    <linearGradient id="heroLine" x1="0" x2="1"><stop offset="0" stop-color="var(--teal)"/><stop offset="1" stop-color="var(--deep)"/></linearGradient>
  </defs>
  <path role="img" aria-label="Photo of a technician servicing a wall-mounted air conditioner while a client watches" d="M0 0H1200V610L600 675L0 615Z" fill="url(#heroPhoto)"/>
  <path d="M0 615L600 675L1200 610" fill="none" stroke="url(#heroLine)" stroke-width="6"/>
</svg>
<div class="hero-copy">
  <h1>Clarovent Services<br>Techniques Grenoble</h1>
  <p>The solution to your<br>maintenance problem</p>
</div>
<a class="btn btn-fill">Read More</a>
<a class="btn btn-light">Get a Quote</a>
<svg class="slider-arrow" style="left:43px" viewBox="0 0 48 48"><circle cx="24" cy="24" r="22" fill="none" stroke="var(--blue)" stroke-width="2"/><path d="M27 14L17 24L27 34" fill="none" stroke="var(--blue)" stroke-width="2.5"/></svg>
<svg class="slider-arrow" style="left:1107px" viewBox="0 0 48 48"><circle cx="24" cy="24" r="23" fill="var(--blue)"/><path d="M21 14L31 24L21 34" fill="none" stroke="#fff" stroke-width="2.5"/></svg>

<!-- about -->
<div class="lead-line" style="left:0;top:841px;width:152px"></div>
<div class="lead-dot" style="left:151px;top:837px"></div>
<h2 class="about-title">ABOUT <span>ROLV</span></h2>
<div class="about-sub">Maintenance of water treatment system</div>
<div class="about-text">
  <p>Lorem Ipsum is simply dummy text of the printing and typesetting industry. Lorem Ipsum has</p>
  <p>industry's standard dummy text ever since the 1500s, when an unknown printer took a galley of type and scrambled Lorem Ipsum is simply dummy text of the printing and typesetting industry.</p>
</div>
<a class="btn btn-outline" style="left:130px;top:1166px;width:168px">Learn More</a>
<svg class="abs" style="left:658px;top:831px" width="410" height="410" viewBox="0 0 410 410">
  <defs><linearGradient id="octRim" x1="0" y1="0" x2="1" y2="1"><stop offset="0" stop-color="var(--teal)"/><stop offset="1" stop-color="var(--deep)"/></linearGradient></defs>
  <polygon points="122,4 288,4 406,122 406,288 288,406 122,406 4,288 4,122" fill="none" stroke="url(#octRim)" stroke-width="5"/>
  <polygon role="img" aria-label="Photo of a technician in a hard hat working on a ceiling ventilation unit" points="130,20 280,20 390,130 390,280 280,390 130,390 20,280 20,130" fill="#b7b9be"/>
</svg>

<!-- services -->
<section class="services">
  <h2 class="section-title">Our <span class="accent">Services</span></h2>
  <div class="service-card" style="left:128px">
    <svg class="icon" width="72" height="72" viewBox="0 0 72 72" fill="none" stroke="#fff" stroke-width="2.5"><path d="M8 18l16-8 16 8v18l-16 8-16-8z M8 18l16 8 16-8 M24 26v18"/><path d="M34 40l14-7 16 8v16l-14 7-16-8z M34 40l16 8 14-7 M50 48v16"/></svg>
    <h3>Air Conditioning</h3>
    <p>Lorem ipsum dolor sit amet, consectetur adipisicing elit, sed do eiusmod tempor</p>
    <svg class="more" width="36" height="36" viewBox="0 0 36 36" fill="none" stroke="#fff" stroke-width="2"><circle cx="18" cy="18" r="16"/><path d="M11 15l7 7 7-7"/></svg>
  </div>
  <div class="service-card featured" style="left:450px">
    <svg class="icon" width="72" height="72" viewBox="0 0 72 72" fill="none" stroke="#fff" stroke-width="2.5"><path d="M36 4l5 18 14-12-5 18 18-2-14 12 14 12-18-2 5 18-14-12-5 18-5-18-14 12 5-18-18 2 14-12L4 26l18 2-5-18 14 12z"/></svg>
    <h3>Heating</h3>
    <p>Lorem ipsum dolor sit amet, consectetur adipisicing elit, sed do eiusmod tempor</p>
    <svg class="more" width="36" height="36" viewBox="0 0 36 36" fill="none" stroke="#fff" stroke-width="2"><circle cx="18" cy="18" r="16"/><path d="M11 15l7 7 7-7"/></svg>
  </div>
  <div class="service-card" style="left:770px">
    <svg class="icon" width="72" height="72" viewBox="0 0 72 72" fill="none" stroke="#fff" stroke-width="2.5"><circle cx="36" cy="36" r="6"/><path d="M36 30C24 26 22 8 36 6s14 16 4 24"/><path d="M42 36c4-12 22-14 24 0s-16 14-24 4"/><path d="M36 42c12 4 14 22 0 24s-14-16-4-24"/><path d="M30 36c-4 12-22 14-24 0s16-14 24-4"/></svg>
    <h3>Air Treatment</h3>
    <p>Lorem ipsum dolor sit amet, consectetur adipisicing elit, sed do eiusmod tempor</p>
    <svg class="more" width="36" height="36" viewBox="0 0 36 36" fill="none" stroke="#fff" stroke-width="2"><circle cx="18" cy="18" r="16"/><path d="M11 15l7 7 7-7"/></svg>
  </div>
</section>

<!-- spirit of service -->
<section class="spirit">
  <svg class="abs" style="left:0;top:0" width="1200" height="558" viewBox="0 0 1200 558">
    <defs><linearGradient id="spiritBg" x1="0" x2="1" y1="0" y2="0"><stop offset="0" stop-color="var(--teal)"/><stop offset=".55" stop-color="var(--blue)"/><stop offset="1" stop-color="var(--deep)"/></linearGradient></defs>
    <rect width="1200" height="558" fill="url(#spiritBg)"/>
    <path role="img" aria-label="Photo of hands holding a refrigerant pressure manifold gauge next to an outdoor AC unit" d="M790 0H1200V558H735C620 430 600 180 790 0Z" fill="#c3c7cb"/>
  </svg>
  <div class="lead-line" style="left:0;top:113px;width:100px;border-color:#fff"></div>
  <div class="lead-dot" style="left:97px;top:109px;background:#fff"></div>
  <div class="spirit-copy">
    <h2>ROLV – The Spirit of Service</h2>
    <div class="sub">Maintenance of water treatment system</div>
    <ul class="checklist">
      <li><svg width="24" height="24" viewBox="0 0 24 24" fill="none" stroke="#fff" stroke-width="2"><path d="M21 11a9 9 0 1 1-4-7"/><path d="M7 11l4 4 10-10"/></svg>Soft water</li>
      <li><svg width="24" height="24" viewBox="0 0 24 24" fill="none" stroke="#fff" stroke-width="2"><path d="M21 11a9 9 0 1 1-4-7"/><path d="M7 11l4 4 10-10"/></svg>Maintenance of softeners</li>
      <li><svg width="24" height="24" viewBox="0 0 24 24" fill="none" stroke="#fff" stroke-width="2"><path d="M21 11a9 9 0 1 1-4-7"/><path d="M7 11l4 4 10-10"/></svg>Treatment of liquid effluents</li>
      <li><svg width="24" height="24" viewBox="0 0 24 24" fill="none" stroke="#fff" stroke-width="2"><path d="M21 11a9 9 0 1 1-4-7"/><path d="M7 11l4 4 10-10"/></svg>Calibration of pH probes</li>
      <li><svg width="24" height="24" viewBox="0 0 24 24" fill="none" stroke="#fff" stroke-width="2"><path d="M21 11a9 9 0 1 1-4-7"/><path d="M7 11l4 4 10-10"/></svg>Conductivity probe calibration</li>
      <li><svg width="24" height="24" viewBox="0 0 24 24" fill="none" stroke="#fff" stroke-width="2"><path d="M21 11a9 9 0 1 1-4-7"/><path d="M7 11l4 4 10-10"/></svg>Analog level management</li>
    </ul>
  </div>
  <div class="abs" style="left:295px;top:460px;height:70px;border-left:2px dashed #fff"></div>
  <div class="lead-dot" style="left:291px;top:528px;background:#fff"></div>
</section>

<!-- climate control -->
<section class="climate">
  <h2 class="section-title">Reversible&nbsp; Climate Control</h2>
  <div class="title-rule"></div>
</section>
<svg class="abs" style="left:418px;top:2710px" width="320" height="290" viewBox="0 0 320 290" fill="none" stroke="#fff" stroke-width="2">
  <circle cx="160" cy="145" r="108"/>
  <path d="M84 69L44 25 M236 69L276 25 M84 221L44 265 M236 221L276 265"/>
  <g fill="#fff" stroke="none"><circle cx="84" cy="69" r="7"/><circle cx="236" cy="69" r="7"/><circle cx="84" cy="221" r="7"/><circle cx="236" cy="221" r="7"/></g>
</svg>
<div class="hub-name">ROLV</div>

<div class="feature right-align" style="left:67px;top:2678px">
  <h4>Installation</h4>
  <p>Use our body field scanner, at home to uncover why yhou feelthe way you do</p>
  <a class="btn-line">Learn More</a>
</div>
<div class="icon-disc" style="left:342px;top:2682px"><svg width="54" height="54" viewBox="0 0 54 54" fill="none" stroke="var(--ink)" stroke-width="3"><path d="M10 44L32 22 M22 10a8 8 0 0 0 10 12"/><path d="M44 44L24 24 M12 10l6 6-4 4-6-6"/><path d="M40 36l6 6-4 4-6-6z"/></svg></div>

<div class="feature" style="left:843px;top:2678px">
  <h4>Troubleshooting</h4>
  <p>Use our body field scanner, at home to uncover why yhou feelthe way you do</p>
  <a class="btn-line">Learn More</a>
</div>
<div class="icon-disc" style="left:722px;top:2682px"><svg width="54" height="54" viewBox="0 0 54 54" fill="none" stroke="var(--ink)" stroke-width="3"><rect x="8" y="16" width="38" height="28" rx="4"/><path d="M20 16v-5h14v5 M8 30h38"/><circle cx="27" cy="30" r="4"/></svg></div>

<div class="feature right-align" style="left:67px;top:2900px">
  <h4>Maintenance</h4>
  <p>Use our body field scanner, at home to uncover why yhou feelthe way you do</p>
  <a class="btn-line">Learn More</a>
</div>
<div class="icon-disc" style="left:342px;top:2903px"><svg width="54" height="54" viewBox="0 0 54 54" fill="none" stroke="var(--ink)" stroke-width="3"><circle cx="27" cy="27" r="8"/><path d="M27 6v7 M27 41v7 M6 27h7 M41 27h7 M12 12l5 5 M37 37l5 5 M12 42l5-5 M37 17l5-5"/><circle cx="27" cy="27" r="15"/></svg></div>

<div class="feature" style="left:843px;top:2900px">
  <h4>Soft water</h4>
  <p>Use our body field scanner, at home to uncover why yhou feelthe way you do</p>
  <a class="btn-line">Learn More</a>
</div>
<div class="icon-disc" style="left:722px;top:2903px"><svg width="54" height="54" viewBox="0 0 54 54" fill="none" stroke="var(--ink)" stroke-width="7"><path d="M40 16A16 16 0 1 0 42 34"/><path d="M32 14h12V2" stroke-width="5"/></svg></div>

<!-- contact -->
<section class="contact">
  <h2 class="section-title">Get in Touch</h2>
  <div class="field" style="left:273px;top:132px;width:315px;height:42px">Your Name</div>
  <div class="field" style="left:611px;top:132px;width:316px;height:42px">Email</div>
  <div class="field" style="left:273px;top:200px;width:654px;height:104px">Message</div>
  <a class="btn btn-outline" style="left:516px;top:326px;width:168px">Learn More</a>
</section>

<!-- footer -->
<footer>
  <div class="footer-brand"><span class="brand-mark"></span><span class="brand-name">ROLV</span></div>
  <div class="socials"><span></span><span></span><span></span><span></span></div>
  <div class="foot-col" style="left:422px">
    <h5>Contact Us</h5>
    <div class="contact-row"><svg width="14" height="18" viewBox="0 0 14 18"><path d="M7 1a6 6 0 0 0-6 6c0 4 6 10 6 10s6-6 6-10a6 6 0 0 0-6-6z" fill="#9aa"/><circle cx="7" cy="7" r="2" fill="#fff"/></svg><span>14 Rue des Tilleuls<br>38100 GRENOBLE</span></div>
    <div class="contact-row"><svg width="16" height="16" viewBox="0 0 16 16"><path d="M3 1c1 0 2 3 2 4s-1 1-1 2 3 5 5 5 1-1 2-1 4 1 4 2-1 2-3 2C7 15 1 9 1 4c0-2 1-3 2-3z" fill="#9aa"/></svg><span>04 00 00 12 34</span></div>
    <div class="contact-row"><svg width="16" height="16" viewBox="0 0 16 16" fill="none" stroke="#9aa" stroke-width="1.5"><rect x="1" y="4" width="14" height="10"/><path d="M1 4l7 5 7-5"/></svg><span>info@rolv-services.fr</span></div>
  </div>
  <div class="foot-col" style="left:740px">
    <h5>Company</h5>
    <ul><li>Home</li><li>About Us</li><li>Achievements</li><li>Contact Us</li></ul>
  </div>
  <div class="foot-col" style="left:948px">
    <h5>Services</h5>
    <ul><li>Air Conditioning</li><li>Heating</li><li>Air Treatment</li><li>Testimonials</li></ul>
  </div>
  <div class="legal">© 2020 ROLV Services Techniques. All Rights are Reserved.</div>
</footer>

</body>
</html>
```